Halvercott Orthodontics business card

Using our existing logo (created with ArtFolio), please create a tasteful, contemporary business card. We are father and daughter orthodontists specializing in braces, clarafit, etc to design healthy, beautiful smiles for children, adolescents, and adults. We would like the design to be family-friendly but not childish.
The final design should include all of the information without looking cluttered (I hope! If necessary to achieve an optimal design, please consider making the card double-sided)
Purple, black, silver on a white card
Please include the following information:
Halvercott Orthodontics (logo)
Marguerite L. Halvercott, DMD
Douglas R. Halvercott, DMD

312 Bramblewood Street
North Andover, MA 01899
978.555.0142

847C Quarry Hollow Street
Methuen, MA 01898
978.555.0187

email frontdesk@halvercottortho.example
website www.halvercottortho.example

```html
<!DOCTYPE html>
<html lang="en">
<head>
<meta charset="utf-8">
<title>Halvercott Orthodontics business card</title>
<link href="https://fonts.googleapis.com/css2?family=Montserrat:wght@400;500;600;700&display=swap" rel="stylesheet">
<style>
  :root {
    --purple: #652b8a;
    --grey-dark: #808080;
    --grey-light: #d1d2d4;
    --grey-shadow: #c9c9cc;
    --ink: #1c1c1c;
    --white: #ffffff;
    --backdrop: #ececec;
  }
  * { margin: 0; padding: 0; box-sizing: border-box; }
  html, body { width: 1200px; height: 938px; overflow: hidden; }
  body {
    background: var(--backdrop);
    font-family: "Montserrat", sans-serif;
    position: relative;
  }
  .card {
    position: absolute;
    left: 220px;
    width: 935px;
    height: 535px;
    transform-origin: 0 0;
    transform: scale(0.8128);
    background: var(--white);
    overflow: hidden;
    box-shadow: 0 6px 18px rgba(0,0,0,0.18);
  }
  .card--front { top: 22px; }
  .card--back { top: 481px; }
  .card__art { position: absolute; inset: 0; }

  /* Front */
  .brand {
    position: absolute;
    left: 0; right: 0;
    top: 232px;
    display: flex;
    align-items: center;
    justify-content: center;
    gap: 18px;
  }
  .brand__dot {
    width: 34px; height: 34px;
    border-radius: 50%;
    background: var(--purple);
  }
  .brand__name {
    font-weight: 600;
    font-size: 44px;
    color: var(--purple);
    letter-spacing: 0.5px;
  }
  .band-text {
    position: absolute;
    left: 0; right: 0;
    top: 444px;
    height: 46px;
    display: flex;
    align-items: center;
    justify-content: center;
    gap: 16px;
    color: var(--white);
    font-size: 21px;
    letter-spacing: 1.6px;
  }
  .band-text svg { width: 26px; height: 26px; }
  .band-text .icon-mail { width: 33px; height: 24px; }

  /* Back */
  .doctors {
    position: absolute;
    right: 68px;
    top: 64px;
    text-align: right;
    color: var(--ink);
    font-size: 31px;
    line-height: 49px;
  }
  .doctors__given { font-weight: 700; }
  .doctors__family { font-weight: 400; }
  .doctors__title { font-size: 20px; font-weight: 500; }
  .office {
    position: absolute;
    right: 163px;
    text-align: right;
    color: var(--ink);
    font-size: 22px;
    line-height: 32.5px;
    font-style: normal;
  }
  .office--one { top: 185px; }
  .office--two { top: 302px; }
</style>
</head>
<body>

<section class="card card--front" aria-label="Card front">
  <svg class="card__art" viewBox="0 0 935 535" aria-hidden="true">
    <rect x="0" y="0" width="935" height="67" fill="var(--grey-dark)"/>
    <rect x="0" y="444" width="935" height="46" fill="var(--purple)"/>
    <rect x="0" y="490" width="935" height="45" fill="var(--grey-light)"/>
  </svg>
  <div class="brand">
    <span class="brand__dot"></span>
    <span class="brand__name">Halvercott Orthodontics</span>
  </div>
  <div class="band-text">
    <svg viewBox="0 0 24 24" fill="none" stroke="#fff" stroke-width="1.5" aria-hidden="true">
      <circle cx="12" cy="12" r="10"/><ellipse cx="12" cy="12" rx="4.5" ry="10"/>
      <path d="M2 12h20M4 7h16M4 17h16"/>
    </svg>
    <span class="band-text__url">www.halvercottortho.example</span>
    <svg viewBox="0 0 24 24" fill="none" stroke="#fff" stroke-width="1.5" aria-hidden="true">
      <circle cx="12" cy="12" r="10"/><ellipse cx="12" cy="12" rx="4.5" ry="10"/>
      <path d="M2 12h20M4 7h16M4 17h16"/>
    </svg>
  </div>
</section>

<section class="card card--back" aria-label="Card back">
  <svg class="card__art" viewBox="0 0 935 535" aria-hidden="true">
    <rect x="0" y="444" width="935" height="91" fill="var(--grey-dark)"/>
    <path d="M935 372 C870 410 800 438 720 444 L935 444 Z" fill="var(--grey-dark)"/>
    <path d="M500 0 C380 110 300 240 330 380 C350 460 420 520 560 535 L380 535 C300 470 250 380 262 270 C275 160 360 60 430 0 Z" fill="var(--grey-shadow)"/>
    <path d="M0 0 L465 0 C360 100 270 220 268 330 C268 420 320 490 390 535 L0 535 Z" fill="var(--purple)"/>
    <path d="M0 375 L92 444 L0 444 Z" fill="var(--grey-dark)"/>
    <rect x="0" y="444" width="935" height="46" fill="var(--purple)"/>
    <path d="M0 490 L935 490 L935 535 L390 535 C360 515 330 500 300 490 Z" fill="var(--grey-dark)"/>
    <path d="M300 490 C330 500 360 515 390 535 L0 535 L0 490 Z" fill="var(--purple)"/>
    <path d="M430 535 C560 520 680 505 770 490 L800 490 C700 515 600 530 520 535 Z" fill="var(--white)" opacity="0.9"/>
    <line x1="813" y1="168" x2="813" y2="444" stroke="var(--purple)" stroke-width="4"/>
    <g fill="var(--purple)">
      <circle cx="813" cy="203" r="16"/>
      <circle cx="813" cy="320" r="16"/>
    </g>
    <g fill="none" stroke="#fff" stroke-width="2.4">
      <path d="M813 213 C807 206 806 203 806 199 A7 7 0 0 1 820 199 C820 203 819 206 813 213 Z"/>
      <path d="M813 330 C807 323 806 320 806 316 A7 7 0 0 1 820 316 C820 320 819 323 813 330 Z"/>
    </g>
    <circle cx="813" cy="199" r="2.3" fill="#fff"/>
    <circle cx="813" cy="316" r="2.3" fill="#fff"/>
  </svg>

  <div class="doctors">
    <div><span class="doctors__given">Marguerite L.</span> <span class="doctors__family">Halvercott,</span> <span class="doctors__title">DMD</span></div>
    <div><span class="doctors__given">Douglas R.</span> <span class="doctors__family">Halvercott,</span> <span class="doctors__title">DMD</span></div>
  </div>

  <address class="office office--one">
    312 Bramblewood Street<br>North Andover, MA 01899<br>978.555.0142
  </address>
  <address class="office office--two">
    847C Quarry Hollow Street<br>Methuen, MA 01898<br>978.555.0187
  </address>

  <div class="band-text">
    <svg class="icon-mail" viewBox="0 0 30 22" aria-hidden="true">
      <rect x="1" y="1" width="28" height="20" fill="none" stroke="#fff" stroke-width="2"/>
      <path d="M1 1 L15 13 L29 1 M1 21 L11 10 M29 21 L19 10" fill="none" stroke="#fff" stroke-width="2"/>
    </svg>
    <span class="band-text__email">frontdesk@halvercottortho.example</span>
    <svg class="icon-mail" viewBox="0 0 30 22" aria-hidden="true">
      <rect x="1" y="1" width="28" height="20" fill="none" stroke="#fff" stroke-width="2"/>
      <path d="M1 1 L15 13 L29 1 M1 21 L11 10 M29 21 L19 10" fill="none" stroke="#fff" stroke-width="2"/>
    </svg>
  </div>
</section>

</body>
</html>
```